Design an attractive wine label for Brell Fine Wines

we need a wine label design, we are an Australian wine exporting company'Brell Fine Wines'. We succeed several pallets in last few months and is going to launch our first container. So it’s time to start our own brands. we will have some wines display in China's shopping mall shelves, so we want to have a catchy label which can attract Chinese eyes immediately. other details you will see in the file i uploaded. The design should include a front and back label.

Target Market(s)

Brell Fine Wines are targeting middle class wine drinkers in 2nd-4th tier Chinese cities.

Colors

Designer to choose colors to be used in the design.

Requirements
Must have
• We’d like something that at first glance is Australian (element, style or color…) but subconsciously connects to the Chinese. Demeanor bearing in mind the demographics targeted across the ranges. We would expect the designs and naming to becoming more formalized as they rise to platinum.
Nice to have
• creative things come out
Should not have
• any dead related word or icon, no number '4' related word or icon, no skull related word or icon, kangaroo (see brand 'Copper vine')

```html
<!DOCTYPE html>
<html lang="en">
<head>
<meta charset="utf-8">
<title>Brell Fine Wines – Label Range</title>
<link rel="stylesheet" href="https://fonts.googleapis.com/css2?family=Cinzel:wght@400;500&display=swap">
<style>
  :root {
    --page-bg: #e9eaeb;
    --cream-light: #f3f0e6;
    --cream-dark: #d9d3c2;
    --ink: #231f1c;
    --black-label: #0c0c0c;
    --gold: #c9963f;
    --gold-light: #e8c27a;
    --orange: #e98a1c;
    --orange-deep: #c4461c;
    --maroon: #7b1f24;
    --maroon-soft: #a4524f;
    --white-soft: #f1ece2;
  }
  * { margin: 0; padding: 0; box-sizing: border-box; }
  html, body {
    width: 1185px; height: 1200px; overflow: hidden;
    background: var(--page-bg);
  }
  .range {
    width: 1185px; height: 1200px;
    display: flex;
    justify-content: center;
    align-items: center;
    gap: 95px;
  }
  .label {
    width: 250px; height: 460px;
    display: flex;
    flex-direction: column;
    align-items: center;
    padding-top: 30px;
    font-family: 'Cinzel', serif;
    box-shadow: 0 2px 10px rgba(0,0,0,0.12);
  }
  .label--cream {
    background: linear-gradient(90deg, var(--cream-dark) 0%, var(--cream-light) 45%, var(--cream-light) 60%, var(--cream-dark) 100%);
    color: var(--ink);
  }
  .label--black {
    background: var(--black-label);
    color: var(--white-soft);
  }
  .range-dot { width: 11px; height: 11px; flex: none; }
  .vintage {
    margin-top: 14px;
    font-size: 12px;
    line-height: 16px;
    letter-spacing: 0.04em;
  }
  .brand-name {
    margin-top: 38px;
    font-size: 32px;
    font-weight: 400;
    letter-spacing: 0.01em;
    line-height: 36px;
    white-space: nowrap;
  }
  .label--black .brand-name { color: var(--gold); }
  .brand-rule {
    width: 150px; height: 1px;
    margin-top: 6px;
    background: currentColor;
    opacity: 0.8;
  }
  .label--black .brand-rule { background: var(--gold); }
  .vineyard-art {
    margin-top: 48px;
    width: 178px; height: 125px;
    border-radius: 6px;
    flex: none;
  }
  .vineyard-art--orange { background: linear-gradient(180deg, var(--orange-deep) 0%, var(--orange) 55%, rgba(233,138,28,0.55) 100%); }
  .vineyard-art--maroon { background: linear-gradient(180deg, var(--maroon) 0%, var(--maroon-soft) 100%); }
  .vineyard-art--gold { background: linear-gradient(180deg, var(--gold-light) 0%, var(--gold) 55%, #6e4f1c 100%); }
  .varietal {
    margin-top: 38px;
    font-size: 16px;
    line-height: 20px;
    font-weight: 500;
    letter-spacing: 0.03em;
    white-space: nowrap;
  }
  .label--black .varietal { font-size: 20px; margin-top: 34px; }
</style>
</head>
<body>
<main class="range">

  <section class="label label--cream">
    <svg class="range-dot" viewBox="0 0 12 12" aria-hidden="true">
      <circle cx="6" cy="6" r="5.5" fill="var(--orange)"/>
      <path d="M6 0.5 A5.5 5.5 0 0 1 6 11.5 Z" fill="var(--orange-deep)"/>
    </svg>
    <p class="vintage">Vintage 2008</p>
    <h2 class="brand-name">Wirrana</h2>
    <div class="brand-rule"></div>
    <div class="vineyard-art vineyard-art--orange" role="img" aria-label="Engraved vineyard rows with a farmhouse and a grape-vine garland in orange tones"></div>
    <p class="varietal">Cabernet Sauvignon</p>
  </section>

  <section class="label label--cream">
    <svg class="range-dot" viewBox="0 0 12 12" aria-hidden="true">
      <circle cx="6" cy="6" r="5.5" fill="var(--maroon)"/>
    </svg>
    <p class="vintage">Vintage 2007</p>
    <h2 class="brand-name">Yarrindel</h2>
    <div class="brand-rule"></div>
    <div class="vineyard-art vineyard-art--maroon" role="img" aria-label="Engraved vineyard rows with a farmhouse and a grape-vine garland in maroon tones"></div>
    <p class="varietal">Cabernet Sauvignon</p>
  </section>

  <section class="label label--black">
    <svg class="range-dot" viewBox="0 0 12 12" aria-hidden="true">
      <circle cx="6" cy="6" r="5" fill="none" stroke="var(--gold-light)" stroke-width="1"/>
      <path d="M6 1 A5 5 0 0 1 6 11 Z" fill="var(--gold-light)"/>
    </svg>
    <p class="vintage">Vintage 2007</p>
    <h2 class="brand-name">Yarrindel</h2>
    <div class="brand-rule"></div>
    <div class="vineyard-art vineyard-art--gold" role="img" aria-label="Engraved vineyard rows with a farmhouse and a grape-vine garland in gold foil"></div>
    <p class="varietal">Merlot</p>
  </section>

</main>
</body>
</html>
```